Business Card Design Project (Beer industry)

I am seeking a redesign of my business card. I am looking for something that will really stand out in both texture and feel. Something more on the modern side then traditional. Nothing die cut shaped like a beer mug please.

The card is used mostly for other industry professionals, as well as bar and restaurant owners. My title is Strategy & Acquisitions. If you would like to somehow incorporate that theme, that may work.

My business is craft and imported beer. Nothing fizzy and yellow, so my products are more on the upscale side.
Updates

I was able to update my logo in .ai and .tif format. I hope that helps. 

Thank you all for your creative ideas. I have uploaded my current business card in pdf format, as well as our logo in .eps file format. We are excited about the submissions so far and want to thank you all again.

PS Please do not include fax number in future submissions, as we are looking for something more creative and a fax says 1999 and not 2015, which is the message we are going for, without being futuristic. 

Thank you all once again for all of your submissions. If we would consider a two sided card, we would like the opposite side not to be the same as the front. The styles we have seen so far, it appears the front and back are too similar. Again, a two sided card is not required. Thank you and we look forward to pushing the boundaries of your creativity. Cheers

Target Market(s)

My card would mostly go to bar and restaurant operators as well as other beer industry professionals

Industry/Entity Type

Restaurant

Requirements
Nice to have
• Two sided would be considered, although not required
Should not have
• Anything die cut shaped like a beer mug.

```html
<!DOCTYPE html>
<html lang="en">
<head>
<meta charset="utf-8">
<title>Kestrel Beer – Business Card</title>
<link rel="stylesheet" href="https://fonts.googleapis.com/css2?family=Questrial&family=Oswald:wght@600&display=swap">
<style>
  :root {
    --page-bg: #f3efe9;
    --card-bg: #ffffff;
    --navy: #1f3563;
    --navy-soft: #2c4a86;
    --brand-red: #9b1e1e;
    --accent-orange: #f0901e;
    --gold: #e9b52d;
    --text-navy: #26335c;
    --white: #ffffff;
  }
  * { box-sizing: border-box; margin: 0; padding: 0; }
  html, body {
    width: 1200px; height: 1158px; overflow: hidden;
    background: var(--page-bg);
  }
  .card {
    position: absolute; left: 300px; top: 99px;
    width: 600px; height: 960px;
    background: var(--card-bg);
    border-radius: 30px; overflow: hidden;
    font-family: "Questrial", sans-serif;
    color: var(--text-navy);
    box-shadow: 0 2px 10px rgba(0,0,0,0.12);
  }
  .skyline-art {
    position: absolute; left: 90px; top: 28px;
    width: 420px; height: 250px;
    border-radius: 8px;
    background: linear-gradient(180deg, var(--navy-soft) 0%, #3e64a8 55%, var(--gold) 100%);
    opacity: 0.9;
  }
  .brand-name {
    position: absolute; left: 0; top: 300px; width: 100%;
    text-align: center;
    font-family: "Oswald", sans-serif; font-weight: 600;
    font-size: 72px; line-height: 100px; letter-spacing: 2px;
    color: var(--brand-red);
  }
  .person { position: absolute; top: 546px; width: 100%; text-align: center; }
  .person-name { font-size: 31px; line-height: 38px; color: var(--brand-red); }
  .person-title { font-size: 21px; line-height: 28px; margin-top: 2px; }
  .direct {
    position: absolute; top: 666px; width: 100%;
    text-align: center; font-size: 22px; line-height: 40px;
  }
  .direct .value { color: var(--brand-red); }
  .direct .cell-value { font-size: 28px; letter-spacing: 1px; }
  .office {
    position: absolute; top: 794px; left: 30px; right: 33px;
    display: flex; justify-content: space-between; align-items: flex-start;
    font-size: 22px; line-height: 33px;
  }
  .office-address { font-style: normal; }
  .office-phone { text-align: right; }
  .rule-orange {
    position: absolute; left: 0; top: 868px; width: 100%; height: 8px;
    background: var(--accent-orange);
  }
  .web-band {
    position: absolute; left: 0; top: 886px; width: 100%; height: 74px;
    background: var(--navy);
    display: flex; align-items: center; justify-content: center;
  }
  .web-address { font-size: 40px; color: var(--white); letter-spacing: 1px; }
</style>
</head>
<body>
  <main class="card">
    <div class="skyline-art" role="img" aria-label="Illustrated city skyline with a statue, stars, wheat stalks and a glass of beer"></div>
    <div class="brand-name">KESTREL BEER</div>

    <section class="person">
      <p class="person-name">Dan Holvik</p>
      <p class="person-title">Strategy &amp; Acquisitions</p>
    </section>

    <section class="direct">
      <p>Cell: <span class="value cell-value">(917) 555-0148</span></p>
      <p>Email: <span class="value">holvik@kestrelmail.com</span></p>
    </section>

    <section class="office">
      <address class="office-address">48 Varick Lane<br>Brooklyn, NY 11222</address>
      <p class="office-phone">Phone: (718) 555-0190</p>
    </section>

    <div class="rule-orange"></div>
    <footer class="web-band">
      <span class="web-address">www.kestrelbeerusa.com</span>
    </footer>
  </main>
</body>
</html>
```